Delcourt Realty Business Cards

Design business card

Target Market(s)

High-End Buyer of Real Estate over $1 million dollars

Industry/Entity Type

Realtor

Contact Information for Business Card

Lena Delcourt R(S) LIC.# 41972
Cell 555 246-1938
Email Lena@Delcourt.example
Website IsleFreshHomes.example

Also Need Cards for:

Hank Delcourt R(B) LIC# 69418
C 555 613-7052
E Hank@Delcourt.example
W IsleFreshHomes.example

Colors

Designer to choose colors to be used in the design.

Requirements
Must have
• Address on back:
• 287 Pohaku Cir. , Port Avela KX 00412
• Logo on back
Nice to have
• I would like the phone numbers and email address to be big so people can read it easily
Should not have
• Very small print Except For: address (287 Pohaku Cir. Wailea HI 96753)

```html
<!DOCTYPE html>
<html lang="en">
<head>
<meta charset="utf-8">
<title>Delcourt Realty Business Cards</title>
<link href="https://fonts.googleapis.com/css2?family=Open+Sans:wght@400;600;700&display=swap" rel="stylesheet">
<style>
  :root {
    --backdrop: #2b2a2a;
    --card-black: #070707;
    --card-white: #ffffff;
    --silver: #b9b9b9;
    --ink: #111111;
    --photo-top: #c98a62;
    --photo-bottom: #d8346e;
  }
  html, body {
    margin: 0;
    width: 1200px;
    height: 1200px;
    overflow: hidden;
    background: var(--backdrop);
    font-family: "Open Sans", sans-serif;
  }
  .canvas { position: relative; width: 1200px; height: 1200px; }
  .card {
    position: absolute;
    width: 700px;
    height: 400px;
    overflow: hidden;
    box-sizing: border-box;
  }
  /* Back of card */
  .card--back { left: 130px; top: 120px; background: var(--card-black); }
  .back-brand {
    position: absolute; left: 0; right: 0; top: 150px;
    display: flex; justify-content: center; align-items: center; gap: 20px;
  }
  .brand-square { width: 46px; height: 46px; background: var(--silver); flex: none; }
  .back-brand .brand-name {
    color: var(--silver); font-weight: 600; font-size: 42px;
    letter-spacing: 4px; text-transform: uppercase; line-height: 1;
  }
  .back-address {
    position: absolute; left: 0; right: 0; bottom: 48px; margin: 0;
    text-align: center; color: var(--silver); font-size: 15px;
    letter-spacing: 1.5px; text-transform: uppercase;
  }
  /* Front of card */
  .card--front { left: 370px; top: 660px; background: var(--card-white); }
  .front-brand {
    position: absolute; right: 30px; top: 44px;
    display: flex; align-items: center; gap: 14px;
  }
  .front-brand .brand-square { width: 34px; height: 34px; background: var(--ink); }
  .front-brand .brand-name {
    color: var(--ink); font-weight: 600; font-size: 30px;
    letter-spacing: 3px; text-transform: uppercase; line-height: 1;
  }
  .agent-photo {
    position: absolute; left: 0; top: 140px; width: 240px; height: 260px;
    background: linear-gradient(180deg, var(--photo-top) 0%, var(--photo-top) 55%, var(--photo-bottom) 100%);
  }
  .bottom-band {
    position: absolute; left: 240px; right: 0; bottom: 0; height: 30px;
    background: var(--ink);
  }
  .name-row {
    position: absolute; left: 262px; right: 0; top: 166px;
    display: flex; align-items: center; gap: 14px;
  }
  .agent-name {
    margin: 0; flex: none;
    font-weight: 700; font-size: 22px; letter-spacing: 2px; line-height: 1.2;
    text-transform: uppercase; color: var(--ink);
  }
  .name-rule { flex: 1; height: 2px; background: var(--ink); margin-top: 6px; }
  .contact-list {
    position: absolute; left: 262px; top: 206px; margin: 0; padding: 0;
    list-style: none; color: var(--ink); font-size: 19px; letter-spacing: 0.5px;
  }
  .contact-list li { display: flex; align-items: center; gap: 10px; height: 32px; }
  .contact-icon { width: 18px; height: 18px; flex: none; }
</style>
</head>
<body>
<main class="canvas">
  <section class="card card--back" aria-label="Card back">
    <div class="back-brand">
      <span class="brand-square"></span>
      <span class="brand-name">Delcourt Realty</span>
    </div>
    <p class="back-address">287 Pohaku Cir. , Port Avela KX 00412</p>
  </section>

  <section class="card card--front" aria-label="Card front">
    <div class="front-brand">
      <span class="brand-square"></span>
      <span class="brand-name">Delcourt Realty</span>
    </div>
    <div class="agent-photo" role="img" aria-label="Portrait photo of the agent"></div>
    <div class="bottom-band"></div>
    <div class="name-row">
      <h1 class="agent-name">Lena Delcourt R(S)</h1>
      <span class="name-rule"></span>
    </div>
    <ul class="contact-list">
      <li>LIC.# 41972</li>
      <li>
        <svg class="contact-icon" viewBox="0 0 18 18" aria-hidden="true"><rect width="18" height="18" rx="3" fill="#111"/><path d="M5 4h2.5l1 3-1.5 1a6 6 0 0 0 3 3l1-1.5 3 1V13a1.5 1.5 0 0 1-1.5 1.5A9 9 0 0 1 3.5 5.5 1.5 1.5 0 0 1 5 4z" fill="#fff"/></svg>
        555 246-1938
      </li>
      <li>
        <svg class="contact-icon" viewBox="0 0 18 18" aria-hidden="true"><rect width="18" height="18" rx="3" fill="#111"/><rect x="3.5" y="5" width="11" height="8" fill="none" stroke="#fff" stroke-width="1.4"/><path d="M3.5 5l5.5 4.5L14.5 5" fill="none" stroke="#fff" stroke-width="1.4"/></svg>
        Lena@Delcourt.example
      </li>
      <li>
        <svg class="contact-icon" viewBox="0 0 18 18" aria-hidden="true"><rect width="18" height="18" rx="3" fill="#111"/><circle cx="9" cy="9" r="5.5" fill="none" stroke="#fff" stroke-width="1.2"/><ellipse cx="9" cy="9" rx="2.3" ry="5.5" fill="none" stroke="#fff" stroke-width="1.2"/><path d="M3.5 9h11" stroke="#fff" stroke-width="1.2"/></svg>
        IsleFreshHomes.example
      </li>
    </ul>
  </section>
</main>
</body>
</html>
```